Torvel, Inc. new buisness cards - brand guide included

We need new business cards. SLEAK SIMPLE FINANCE. They must include a place for NAME, TITLE, CELL, OFFICE PHONE, EMAIL. they also must include our services across the bottom. AIR, OCEAN, FTL, LTL, EXPRESS. for reference this will be being handed to some of the most prestigious shipping companies in a america.

Target Market(s)

Finance and corporate

Contact Information for Business Card

We need new business cards. SLEAK SIMPLE FINANCE. They must include a place for NAME, TITLE, CELL, OFFICE PHONE, EMAIL. they also must include our services across the bottom. AIR, OCEAN, FTL, LTL, EXPRESS.

Requirements
Must have
• We need new business cards. SLEAK SIMPLE FINANCE. They must include a place for NAME, TITLE, CELL, OFFICE PHONE, EMAIL. they also must include our services across the bottom. AIR, OCEAN, FTL, LTL, EXPRESS.
Nice to have
• USE THE COLORS AND LOGO IN THE BRAND GUIDE :)

```html
<!DOCTYPE html>
<html lang="en">
<head>
<meta charset="utf-8">
<title>Torvel, Inc. Business Card</title>
<link rel="stylesheet" href="https://fonts.googleapis.com/css2?family=Montserrat:wght@400;700&display=swap">
<style>
  :root {
    --backdrop: #2b2b2d;
    --card: #141414;
    --gold: #c9b993;
    --silver: #d9d9d9;
    --white: #f2f2f2;
  }
  * { box-sizing: border-box; margin: 0; padding: 0; }
  html, body { width: 1200px; height: 993px; overflow: hidden; }
  body {
    background: var(--backdrop);
    font-family: "Montserrat", sans-serif;
    position: relative;
  }
  .card {
    position: absolute;
    background: var(--card);
    border-radius: 22px;
    box-shadow: 0 12px 30px rgba(0,0,0,.45);
  }
  .card-front {
    left: 50px; top: 336px; width: 560px; height: 320px;
    display: flex; align-items: center; justify-content: center;
  }
  .brand {
    display: flex; align-items: center; gap: 18px;
    font-weight: 700; letter-spacing: 10px;
  }
  .brand-square { width: 22px; height: 22px; }
  .card-front .brand { color: var(--silver); font-size: 58px; }
  .card-front .brand-square { background: var(--silver); }

  .card-back {
    left: 730px; top: 216px; width: 320px; height: 560px;
    display: flex; flex-direction: column; align-items: center;
    padding: 56px 30px 0;
  }
  .card-back .brand { color: var(--gold); font-size: 34px; letter-spacing: 6px; gap: 12px; }
  .card-back .brand-square { background: var(--gold); width: 14px; height: 14px; }
  .person-name {
    margin-top: 92px; color: var(--gold); font-weight: 700;
    font-size: 21px; letter-spacing: .5px;
  }
  .person-title { margin-top: 4px; color: var(--white); font-size: 12px; letter-spacing: .5px; }
  .divider-icons {
    margin-top: 26px; width: 100%; display: flex; align-items: center; gap: 8px;
  }
  .divider-icons .rule { flex: 1; height: 1px; background: var(--gold); }
  .icon { width: 20px; height: 20px; border-radius: 4px; background: var(--gold); display: flex; align-items: center; justify-content: center; }
  .contact-list {
    margin-top: 20px; list-style: none; text-align: center;
    color: var(--white); font-size: 14px; line-height: 1.5; letter-spacing: .5px;
  }
  .contact-rule { margin-top: 20px; width: 100%; height: 1px; background: var(--white); }
  .services {
    margin-top: 20px; color: var(--white); font-size: 12.5px; letter-spacing: .5px;
    display: flex; align-items: center; gap: 6px;
  }
  .services .dot { width: 5px; height: 5px; border-radius: 50%; background: var(--gold); }
</style>
</head>
<body>
  <section class="card card-front" aria-label="Card front">
    <div class="brand"><span class="brand-square"></span>TORVEL</div>
  </section>

  <section class="card card-back" aria-label="Card back">
    <div class="brand"><span class="brand-square"></span>TORVEL</div>
    <h1 class="person-name">Daniel Whitford</h1>
    <p class="person-title">Managing Director</p>
    <div class="divider-icons">
      <span class="rule"></span>
      <span class="icon" aria-label="Cell">
        <svg width="12" height="12" viewBox="0 0 12 12"><rect x="3" y="1" width="6" height="10" rx="1" fill="none" stroke="#141414" stroke-width="1.2"/></svg>
      </span>
      <span class="icon" aria-label="Office phone">
        <svg width="12" height="12" viewBox="0 0 12 12"><path d="M2 4 Q6 1 10 4 L9 5.5 L7.5 4.8 L7.5 4 Q6 3.5 4.5 4 L4.5 4.8 L3 5.5 Z M3 7 H9 V10 H3 Z" fill="#141414"/></svg>
      </span>
      <span class="icon" aria-label="Email">
        <svg width="12" height="12" viewBox="0 0 12 12"><rect x="1.5" y="3" width="9" height="6.5" fill="none" stroke="#141414" stroke-width="1.1"/><path d="M1.5 3 L6 7 L10.5 3" fill="none" stroke="#141414" stroke-width="1.1"/></svg>
      </span>
      <span class="rule"></span>
    </div>
    <ul class="contact-list">
      <li>555-014-2290</li>
      <li>555 018 773</li>
      <li>accounting@torvelinc.com</li>
    </ul>
    <div class="contact-rule"></div>
    <p class="services">
      AIR<span class="dot"></span>OCEAN<span class="dot"></span>FTL<span class="dot"></span>LTL<span class="dot"></span>EXPRESS
    </p>
  </section>
</body>
</html>
```